K&T Holdings

Design a modern simple business card. I have attached a clean version of a card we like form Marrowfield Partners another company we own. I also attached the old K&T card design and logo and a couple of ideas we had but just can't finalize on whether we like them or not. We would like to include the 20 year logo somewhere on the card.

```html
<!DOCTYPE html>
<html lang="en">
<head>
<meta charset="utf-8">
<title>K&amp;T Holdings — Business Card</title>
<link href="https://fonts.googleapis.com/css2?family=Montserrat:wght@400;500;600;700&display=swap" rel="stylesheet">
<style>
  :root {
    --navy: #29255f;
    --grey: #b9b9bb;
    --mid-grey: #858587;
    --white: #ffffff;
    --backdrop: #e9e9ea;
    --font: "Montserrat", Arial, sans-serif;
  }
  * { box-sizing: border-box; margin: 0; padding: 0; }
  html, body {
    width: 1200px; height: 1200px; overflow: hidden;
    background: var(--backdrop);
    font-family: var(--font);
  }
  .canvas { position: relative; width: 1200px; height: 1200px; }
  .card {
    position: absolute; left: 151px; width: 895px; height: 525px;
    background: var(--white); overflow: hidden;
    box-shadow: 0 2px 6px rgba(0,0,0,0.12);
  }
  .card--front { top: 60px; }
  .card--back { top: 619px; }
  .card__art { position: absolute; inset: 0; width: 100%; height: 100%; }

  .wordmark {
    position: absolute; font-weight: 700; color: var(--navy);
    white-space: nowrap; text-align: right; transform: translateY(-50%);
  }
  .card--front .wordmark { right: 312px; top: 146px; font-size: 32px; }
  .card--back .wordmark { right: 460px; top: 265px; font-size: 34px; }

  .anniversary { position: absolute; color: var(--navy); }
  .anniversary__row { display: flex; align-items: center; }
  .anniversary__num { font-weight: 700; line-height: 0.8; letter-spacing: -2px; }
  .anniversary__word { font-weight: 600; color: var(--mid-grey); margin-left: 6px; letter-spacing: 1px; }
  .anniversary__dates { font-weight: 600; color: var(--mid-grey); letter-spacing: 0.5px; margin-top: 8px; }
  .card--front .anniversary { left: 640px; top: 88px; }
  .card--front .anniversary__num { font-size: 96px; }
  .card--front .anniversary__word { font-size: 18px; }
  .card--front .anniversary__dates { font-size: 22px; }
  .card--back .anniversary { left: 488px; top: 196px; }
  .card--back .anniversary__num { font-size: 112px; }
  .card--back .anniversary__word { font-size: 20px; }
  .card--back .anniversary__dates { font-size: 25px; }

  .contact-block {
    position: absolute; right: 76px; top: 268px; text-align: right; color: var(--white);
  }
  .contact-block__name { font-size: 37px; font-weight: 700; line-height: 1.1; }
  .contact-block__title { font-size: 18px; font-weight: 400; margin-top: 4px; }
  .contact-list { list-style: none; margin-top: 34px; right: -28px; position: relative; }
  .contact-list__item {
    display: flex; justify-content: flex-end; align-items: center;
    font-size: 20px; font-weight: 400; line-height: 29px;
  }
  .contact-list__icon { width: 14px; height: 14px; margin-left: 14px; }
</style>
</head>
<body>
<main class="canvas">

  <section class="card card--front">
    <svg class="card__art" viewBox="0 0 895 525" aria-hidden="true">
      <rect x="0" y="241" width="895" height="284" fill="var(--navy)"/>
      <path d="M0,241 L262,241 C274,300 272,380 222,430 C172,478 92,498 0,496 Z" fill="var(--white)"/>
      <path d="M160,102 C200,150 235,200 250,252 C260,320 250,380 215,425 C248,382 258,320 246,252 C232,200 196,150 160,102 Z" fill="var(--grey)" stroke="var(--grey)" stroke-width="3"/>
      <path d="M170,98 C218,140 252,190 266,248 L256,248 C240,196 206,146 170,98 Z" fill="var(--navy)"/>
      <path d="M90,516 C140,512 190,500 232,482 C196,504 150,514 90,516 Z" fill="var(--grey)" stroke="var(--grey)" stroke-width="3"/>
      <line x1="615" y1="70" x2="615" y2="215" stroke="var(--navy)" stroke-width="1.5"/>
    </svg>
    <div class="wordmark">K&amp;T Holdings</div>
    <div class="anniversary">
      <div class="anniversary__row">
        <span class="anniversary__num">20</span>
        <span class="anniversary__word">YEARS</span>
      </div>
      <div class="anniversary__dates">2004-2024</div>
    </div>
    <div class="contact-block">
      <h1 class="contact-block__name">Dylan Whitaker</h1>
      <p class="contact-block__title">President &amp; COO</p>
      <ul class="contact-list">
        <li class="contact-list__item">713-555-0142
          <svg class="contact-list__icon" viewBox="0 0 24 24"><path fill="var(--white)" d="M6.6 10.8a15 15 0 0 0 6.6 6.6l2.2-2.2a1 1 0 0 1 1-.25 11.4 11.4 0 0 0 3.6.57 1 1 0 0 1 1 1V20a1 1 0 0 1-1 1A17 17 0 0 1 3 4a1 1 0 0 1 1-1h3.5a1 1 0 0 1 1 1c0 1.25.2 2.45.57 3.57a1 1 0 0 1-.25 1z"/></svg>
        </li>
        <li class="contact-list__item">8777-555-0163
          <svg class="contact-list__icon" viewBox="0 0 24 24"><rect x="2" y="5" width="20" height="14" rx="1.5" fill="var(--white)"/><path d="M3 6.5l9 6.3 9-6.3" fill="none" stroke="var(--navy)" stroke-width="1.8"/></svg>
        </li>
        <li class="contact-list__item">dylan@marrowfieldpartners.com
          <svg class="contact-list__icon" viewBox="0 0 24 24"><circle cx="12" cy="12" r="10" fill="none" stroke="var(--white)" stroke-width="2"/><path d="M2 12h20M12 2c3 3 3 17 0 20M12 2c-3 3-3 17 0 20" fill="none" stroke="var(--white)" stroke-width="1.6"/></svg>
        </li>
      </ul>
    </div>
  </section>

  <section class="card card--back">
    <svg class="card__art" viewBox="0 0 895 525" aria-hidden="true">
      <path d="M640,40 C770,120 815,300 700,420 C620,495 420,488 268,396 C430,462 620,470 690,402 C780,300 750,130 640,40 Z" fill="var(--grey)"/>
      <path d="M655,31 C790,110 840,300 720,430 C640,510 420,500 261,388 C430,476 645,484 712,412 C806,306 772,122 655,31 Z" fill="var(--navy)"/>
      <line x1="456" y1="175" x2="456" y2="352" stroke="var(--navy)" stroke-width="1.5"/>
    </svg>
    <div class="wordmark">K&amp;T Holdings</div>
    <div class="anniversary">
      <div class="anniversary__row">
        <span class="anniversary__num">20</span>
        <span class="anniversary__word">YEARS</span>
      </div>
      <div class="anniversary__dates">2004-2024</div>
    </div>
  </section>

</main>
</body>
</html>
```